Cutting Costs Quickly - A Weekend Money Plan

Nonfiction book about how to save on insurance. Almost one hundred measures and examples to reduce ones insurance costs.

Target Market(s)

Men/Women between 18 and 50

Industry/Entity Type

Insurance

```html
<!DOCTYPE html>
<html lang="en">
<head>
<meta charset="utf-8">
<title>Cutting Costs Quickly – A Weekend Money Plan</title>
<link rel="stylesheet" href="https://fonts.googleapis.com/css2?family=Archivo+Black&family=Montserrat:wght@600&family=Raleway:wght@300;800&display=swap">
<style>
  :root{
    --stage:#e4e4e4;
    --paper:#ffffff;
    --salmon:#f58a7e;
    --mint:#9adcd2;
    --navy:#2f3e8e;
    --sky:#3bafe4;
    --sky-soft:#a9dbf3;
    --pig:#f7a197;
    --pig-soft:#fbd0ca;
    --author:#7dcbb7;
  }
  *{margin:0;padding:0;box-sizing:border-box}
  html,body{width:1200px;height:1200px;overflow:hidden}
  body{background:radial-gradient(circle at 50% 40%,#f4f4f4,var(--stage));position:relative}

  .cover{position:absolute;left:210px;top:50px;width:780px;height:1100px;background:var(--paper);
    box-shadow:0 10px 40px rgba(0,0,0,.12);overflow:hidden}

  .title{font-weight:normal}
  .title-top{position:absolute;top:62px;width:100%;text-align:center;
    font-family:'Raleway',sans-serif;font-weight:300;font-size:78px;letter-spacing:1px;color:var(--salmon)}

  .title-band{position:absolute;top:178px;left:0;width:100%;height:92px;background:var(--mint);
    display:flex;justify-content:center;align-items:center}
  .title-band span{background:var(--paper);padding:0 26px;height:100%;display:flex;align-items:center;
    font-family:'Raleway',sans-serif;font-weight:800;font-size:78px;letter-spacing:3px;color:var(--navy)}

  .cover-art{position:absolute;top:310px;left:150px;width:480px;height:480px;border-radius:50%;
    background:radial-gradient(circle at 50% 50%,var(--pig) 0%,var(--pig-soft) 26%,var(--sky-soft) 52%,var(--sky) 78%,rgba(59,175,228,0) 100%)}

  .tagline{position:absolute;top:830px;left:0;width:100%;height:170px;display:flex;align-items:stretch}
  .tagline-lead{flex:0 0 430px;background:var(--salmon);display:flex;align-items:center;justify-content:center;
    padding:0 28px;white-space:nowrap;
    font-family:'Archivo Black',sans-serif;font-size:46px;color:var(--paper);letter-spacing:1px}
  .tagline-divider{flex:0 0 30px;display:flex;flex-direction:column;align-items:center;justify-content:center;gap:10px}
  .tagline-divider i{display:block;width:3px;height:52px;background:var(--sky)}
  .tagline-main{flex:1;display:flex;align-items:center;white-space:nowrap;
    font-family:'Archivo Black',sans-serif;font-size:58px;color:var(--sky);letter-spacing:1px}
  .tagline-side{flex:0 0 56px;display:flex;align-items:center;justify-content:center}
  .tagline-side span{transform:rotate(-90deg);font-family:'Montserrat',sans-serif;font-weight:600;
    font-size:28px;letter-spacing:3px;color:var(--salmon)}

  .author{position:absolute;top:1030px;left:0;width:100%;display:flex;align-items:center;justify-content:center;gap:20px}
  .author .rule{flex:1;height:2px;background:var(--mint)}
  .author span{font-family:'Montserrat',sans-serif;font-weight:600;font-size:22px;color:var(--author);letter-spacing:1px}

  .foot-stripes{position:absolute;bottom:18px;left:0;width:100%;height:14px;
    border-top:3px solid var(--mint);border-bottom:3px solid var(--mint)}
</style>
</head>
<body>
  <main class="cover">
    <h1 class="title">
      <span class="title-top">CUTTING COSTS</span>
      <span class="title-band"><span>QUICKLY</span></span>
    </h1>

    <div class="cover-art" role="img" aria-label="Illustration of two blue hands cupped around a pink piggy bank with a gold coin"></div>

    <div class="tagline">
      <div class="tagline-lead">A WEEKEND</div>
      <div class="tagline-divider"><i></i><i></i></div>
      <div class="tagline-main">MONEY</div>
      <div class="tagline-side"><span>PLAN</span></div>
    </div>

    <div class="author"><div class="rule"></div><span>Lukas Brenner</span><div class="rule"></div></div>
    <div class="foot-stripes"></div>
  </main>
</body>
</html>
```